Weightloss company needs Business Card

We want a business card that is clean and professional, yet portrays that we are a friendly, innovative, and versatile program designed to fit the needs of our clients.
I would like there to be 2 sides, one side having an appointment card, and the other side containing the logo and business information. There can be decorations on both sides. The logo is attached.

Target Market(s)

Men and women 40-60

Industry/Entity Type

Business

Contact Information for Business Card

Font styles to use
Sans Serif

Requirements
Must have
• The logo, space for business information
Nice to have
• The colors in the logo
Should not have
• No pictures of people or food

```html
<!DOCTYPE html>
<html lang="en">
<head>
<meta charset="utf-8">
<title>Turnwell Weightloss – Business Card</title>
<link rel="stylesheet" href="https://fonts.googleapis.com/css2?family=Montserrat:wght@400;600;800&family=Open+Sans:wght@400;600&display=swap">
<style>
  :root {
    --brand-red: #e0203f;
    --card-white: #f7f7f7;
    --ink: #2b2b2b;
    --rule: #9a9a9a;
    --page-bg: #e9e6e1;
  }
  * { box-sizing: border-box; margin: 0; padding: 0; }
  html, body { width: 1200px; height: 780px; overflow: hidden; }
  body {
    background: var(--page-bg);
    font-family: "Open Sans", Arial, sans-serif;
    color: var(--ink);
    position: relative;
  }
  .card {
    position: absolute;
    top: 240px;
    width: 520px;
    height: 300px;
    background: var(--card-white);
    box-shadow: 0 6px 18px rgba(0,0,0,.18);
    overflow: hidden;
  }
  .card--front { left: 40px; }
  .card--appointment { left: 640px; }

  /* front side */
  .front-band { position: absolute; inset: 0; }
  .brand-name {
    font-family: "Montserrat", Arial, sans-serif;
    font-weight: 800;
    color: var(--brand-red);
    letter-spacing: .5px;
    white-space: nowrap;
  }
  .front-logo {
    position: absolute;
    left: 120px; top: 70px;
    display: flex; align-items: center; gap: 10px;
    font-size: 26px;
  }
  .brand-dot {
    width: 12px; height: 12px; border-radius: 50%;
    background: var(--brand-red);
  }
  .website {
    position: absolute; left: 300px; top: 228px;
    font-size: 12px; color: var(--brand-red);
    white-space: nowrap;
  }
  .contact {
    position: absolute; left: 36px; bottom: 32px;
    font-size: 13px; line-height: 1.45;
  }
  .contact .employee-name {
    font-family: "Montserrat", Arial, sans-serif;
    font-weight: 600; font-size: 16px; color: var(--brand-red);
  }
  .contact .title { margin-bottom: 12px; }
  .contact-row { display: flex; align-items: center; gap: 6px; }
  .contact-icon { width: 14px; height: 14px; flex: none; }

  /* appointment side */
  .appt-band {
    position: absolute; left: 0; top: 0; width: 100%; height: 110px;
    background: var(--brand-red);
  }
  .appt-logo {
    position: absolute; left: 0; right: 0; top: 36px;
    display: flex; justify-content: center; align-items: center; gap: 10px;
    font-size: 30px;
  }
  .appt-logo .brand-name { color: #fff; }
  .appt-logo .brand-dot { background: #fff; }
  .appt-heading {
    position: absolute; left: 28px; top: 126px;
    font-family: "Montserrat", Arial, sans-serif;
    font-size: 17px; color: var(--brand-red);
  }
  .appt-heading-rule {
    position: absolute; left: 250px; right: 28px; top: 146px;
    border-top: 1px solid var(--rule);
  }
  .days {
    position: absolute; left: 28px; right: 28px; top: 170px;
    display: flex; justify-content: space-between;
  }
  .day { display: flex; align-items: center; gap: 6px; font-size: 12px; color: var(--brand-red); }
  .day-box { width: 16px; height: 16px; border: 1px solid var(--rule); background: #fff; }
  .field {
    position: absolute; left: 28px; right: 28px;
    display: flex; align-items: flex-end; gap: 8px;
    font-size: 13px; color: var(--brand-red);
  }
  .field--date { top: 212px; }
  .field--time { top: 250px; }
  .field-line { flex: 1; border-bottom: 1px solid var(--rule); height: 16px; }
  .meridiem { font-size: 11px; line-height: 1.1; }
</style>
</head>
<body>

<section class="card card--front" aria-label="Business card front">
  <svg class="front-band" width="520" height="300" viewBox="0 0 520 300" aria-hidden="true">
    <path d="M462 0 H520 V300 H502 C502 180 492 80 462 0 Z" fill="var(--brand-red)"/>
    <path d="M462 0 C492 80 502 180 502 300" fill="none" stroke="#ffffff" stroke-width="3"/>
  </svg>

  <div class="front-logo">
    <span class="brand-dot"></span>
    <span class="brand-name">Turnwell Weightloss</span>
  </div>

  <div class="website">www.yourwebsite.com</div>

  <div class="contact">
    <div class="employee-name">EMPLOYEE NAME</div>
    <div class="title">Your Title</div>
    <div>PO BOX your address,</div>
    <div>2nd street,USA</div>
    <div class="contact-row">
      <svg class="contact-icon" viewBox="0 0 14 14" aria-hidden="true">
        <rect width="14" height="14" rx="2" fill="var(--brand-red)"/>
        <path d="M4 3.5 C3.5 6.5 6.5 10 10 10.5 L10.5 8.8 L8.8 8 L8 8.8 C6.8 8.2 5.8 7.2 5.2 6 L6 5.2 L5.2 3.5 Z" fill="#fff"/>
      </svg>
      <span>123.456.0000</span>
    </div>
    <div class="contact-row">
      <svg class="contact-icon" viewBox="0 0 14 14" aria-hidden="true">
        <rect width="14" height="14" rx="2" fill="var(--brand-red)"/>
        <rect x="3" y="4" width="8" height="6" fill="none" stroke="#fff" stroke-width="1"/>
        <path d="M3 4 L7 7.5 L11 4" fill="none" stroke="#fff" stroke-width="1"/>
      </svg>
      <span>info@yourgmail.com</span>
    </div>
  </div>
</section>

<section class="card card--appointment" aria-label="Appointment card">
  <div class="appt-band"></div>
  <div class="appt-logo">
    <span class="brand-dot"></span>
    <span class="brand-name">Turnwell Weightloss</span>
  </div>

  <div class="appt-heading">Has An Appointment On</div>
  <div class="appt-heading-rule"></div>

  <div class="days">
    <div class="day"><span class="day-box"></span>Mon</div>
    <div class="day"><span class="day-box"></span>Tues</div>
    <div class="day"><span class="day-box"></span>Wed</div>
    <div class="day"><span class="day-box"></span>Thur</div>
    <div class="day"><span class="day-box"></span>Fri</div>
    <div class="day"><span class="day-box"></span>Sat</div>
  </div>

  <div class="field field--date">
    <span>Date :</span><span class="field-line"></span>
  </div>
  <div class="field field--time">
    <span>Time :</span><span class="field-line"></span>
    <span class="meridiem">am.<br>pm.</span>
  </div>
</section>

</body>
</html>
```